Cards
Brookvale Estate Advisors
Cards - Real Estate
Creative Brief
Modern
Teodoro Villalba
Managing Broker
4870 Hollow Ln. Larkfield OH 46958
closedbytv@quellmark.com
I also need the Homeward/MLS logo, along with the Fair Dwelling logo

```html
<!DOCTYPE html>
<html lang="en">
<head>
<meta charset="utf-8">
<title>Brookvale Estate Advisors – Business Card</title>
<link href="https://fonts.googleapis.com/css2?family=Tinos:wght@400;700&display=swap" rel="stylesheet">
<style>
  :root {
    --backdrop: #2b2b2b;
    --card: #ffffff;
    --ink: #2a2a2a;
    --brand-gray: #4a4a4a;
    --leaf: #6b9a1f;
    --leaf-dark: #5a8718;
    --sky: #3e8fd0;
    --badge: #3a3a3a;
  }
  * { margin: 0; padding: 0; box-sizing: border-box; }
  html, body {
    width: 1200px; height: 780px; overflow: hidden;
    background: var(--backdrop);
    font-family: "Tinos", "Times New Roman", serif;
    color: var(--ink);
  }
  .business-card {
    position: absolute; left: 100px; top: 104px;
    width: 1000px; height: 572px;
    background: var(--card);
    border-radius: 34px;
    overflow: hidden;
  }
  .affiliation-badges {
    position: absolute; top: 44px; right: 52px;
    display: flex; gap: 12px; align-items: center;
  }
  .badge { background: var(--badge); }
  .badge--square { width: 38px; height: 38px; }
  .badge--wide { width: 52px; height: 38px; border-radius: 4px; }
  .badge--small { width: 34px; height: 34px; border-radius: 3px; }
  .brand {
    position: absolute; left: 180px; top: 150px;
    display: flex; align-items: center; gap: 26px;
  }
  .brand-mark { width: 84px; height: 84px; background: var(--leaf); }
  .brand-name {
    font-size: 46px; font-weight: 400; color: var(--brand-gray);
    letter-spacing: 1px; line-height: 1;
  }
  .identity-band {
    position: absolute; left: 0; top: 282px; width: 100%; height: 98px;
    background: var(--leaf);
    border-top: 4px solid var(--sky);
    border-bottom: 4px solid var(--sky);
    text-align: center; color: #fff;
    padding-top: 14px;
  }
  .agent-name { font-size: 36px; font-weight: 700; line-height: 1.1; }
  .agent-title { font-size: 22px; margin-top: 4px; }
  .contact-block {
    position: absolute; left: 0; top: 408px; width: 100%;
    text-align: center; font-size: 24px; line-height: 1.55;
  }
  .phone-line { display: flex; justify-content: center; gap: 24px; align-items: center; }
  .phone-item { display: inline-flex; align-items: center; gap: 6px; }
  .phone-item svg { width: 20px; height: 22px; fill: var(--leaf-dark); }
</style>
</head>
<body>
  <main class="business-card">
    <div class="affiliation-badges">
      <span class="badge badge--square" aria-label="Homeward membership badge"></span>
      <span class="badge badge--wide" aria-label="MLS listing badge"></span>
      <span class="badge badge--small" aria-label="Fair Dwelling badge"></span>
    </div>

    <div class="brand">
      <span class="brand-mark"></span>
      <span class="brand-name">Brookvale Estate Advisors</span>
    </div>

    <section class="identity-band">
      <h1 class="agent-name">Teodoro Villalba</h1>
      <p class="agent-title">Managing Broker</p>
    </section>

    <section class="contact-block">
      <p class="address">4870 Hollow Ln., Larkfield OH 46958</p>
      <p class="phone-line">
        <span class="phone-item">
          <svg viewBox="0 0 20 22" aria-hidden="true"><path d="M4 2c1-1 2-1 3 0l2 3c.5 1 .3 2-.5 2.6L7.3 8.5c1 2.4 2.8 4.4 5 5.6l1-1.2c.7-.8 1.7-.9 2.6-.3l3 2c1 .7 1 1.7.2 2.6l-1.6 1.7C15 21 9 18 5 13S1 4 4 2z"/></svg>
          555-210-3847
        </span>
        <span class="phone-item">
          <svg viewBox="0 0 20 22" aria-hidden="true"><path d="M5 1h10a2 2 0 0 1 2 2v16a2 2 0 0 1-2 2H5a2 2 0 0 1-2-2V3a2 2 0 0 1 2-2zm0 3v12h10V4zm5 13.5a1.2 1.2 0 1 0 0 2.4 1.2 1.2 0 0 0 0-2.4z"/></svg>
          555-274-9163
        </span>
        <span class="phone-item">
          <svg viewBox="0 0 20 22" aria-hidden="true"><path d="M5 2h8l2 2v4H5zM2 9h16a1 1 0 0 1 1 1v7h-3v3H4v-3H1v-7a1 1 0 0 1 1-1zm4 6v3h8v-3z"/></svg>
          555-308-7521
        </span>
      </p>
      <p class="email">closedbytv@quellmark.com</p>
    </section>
  </main>
</body>
</html>
```